Brightwell Giving Inc

We need a full re-design of our non-profit organization website (www.brightwellgiving.org). Ideally, we are looking to make it more attractive, user-friendly, and interactive with our business model.

Please make sure to user colors that ago with our logo.

We need a homepage done and we also need a content page done where we will use for the other pages to fill with content.

Target Market(s)

Clothes/textiles donations.

Industry/Entity Type

Charity

Number of Pages Required

2 page

Colors

Designer to choose colors to be used in the design.

Requirements
Must have
• It must match the styling of our logo and same colors as current website. (www.brightwellgiving.org)
Nice to have
• Sleek homepage that is easy to understand and get our main points across.

```html
<!DOCTYPE html>
<html lang="en">
<head>
<meta charset="utf-8">
<title>Brightwell Giving – Mission</title>
<link href="https://fonts.googleapis.com/css2?family=Roboto:wght@400;500;700;900&display=swap" rel="stylesheet">
<style>
:root{
  --gold:#f5c300;
  --ink:#1a1a1a;
  --text:#2b2b2b;
  --bar:#1d1d1d;
  --rule:#e6e6e6;
  --mapbar:#4d6670;
  --white:#ffffff;
  --brand:#2f6d2a;
}
*{box-sizing:border-box;margin:0;padding:0}
html,body{width:1200px;height:2276px;overflow:hidden;background:var(--white)}
body{font-family:'Roboto',Arial,sans-serif;color:var(--text);position:relative}
.abs{position:absolute}
.topbar{left:0;top:0;width:1200px;height:40px;background:var(--bar);color:var(--white);font-size:11px;font-weight:700}
.topbar .phone{top:14px}
.search{left:880px;top:8px;width:192px;height:24px;background:#555;border-radius:4px;font-size:10.5px;font-weight:500;color:#eee;padding:6px 10px}
.search svg{position:absolute;right:8px;top:5px}
.header{left:0;top:40px;width:1200px;height:82px;border-bottom:1px solid var(--rule)}
.brand{left:127px;top:20px;display:flex;align-items:center;gap:10px}
.brand .mark{width:34px;height:34px;background:var(--gold)}
.brand .name{font-size:22px;font-weight:700;color:var(--brand);line-height:1}
.tagline{left:171px;top:52px;font-size:11px;color:#333}
.nav{top:37px;font-size:10.5px;font-weight:700;color:var(--ink);letter-spacing:.2px}
.donate{left:1009px;top:28px;width:62px;height:29px;background:var(--gold);border-radius:3px;font-size:10.5px;font-weight:700;text-align:center;line-height:29px;color:var(--ink)}
.crumb{left:127px;top:153px;font-size:10px;font-weight:500;color:#555}
.crumb span{color:var(--gold)}
.photo{display:block}
.mission-card{left:668px;top:255px;width:406px;height:268px;background:var(--white);padding:22px 26px 22px 28px}
.h-gold{font-size:26px;font-weight:900;color:var(--gold)}
.body{font-size:12px;line-height:21px;color:var(--text)}
.mission-card .body{margin-top:8px;font-size:11.6px}
.impact{left:127px;top:575px;width:947px}
.impact .body{margin-top:10px;font-size:11.6px}
.divider{left:127px;top:774px;width:947px;height:1px;background:var(--rule)}
.story{width:450px}
.story h2{font-size:24px;font-weight:500;color:var(--ink);margin-bottom:16px}
.more{display:block;margin-top:26px;font-size:12px;font-weight:500;color:var(--gold);text-transform:uppercase}
.video-title{left:141px;top:842px;color:var(--white);font-size:18px}
.mapbar{left:0;top:1934px;width:1200px;height:38px;background:var(--mapbar);color:var(--white);font-size:15px;font-weight:500}
.map{left:0;top:1972px;width:1200px;height:250px}
.footer{left:0;top:2222px;width:1200px;height:54px;background:var(--bar);color:var(--white);font-size:10px;font-weight:500}
</style>
</head>
<body>

<div class="abs topbar">
  <div class="abs phone" style="left:127px">TOLL FREE: (855) 401-7739</div>
  <div class="abs phone" style="left:287px">NEW YORK: 518-555-0192</div>
  <div class="abs search">Find Local Donation Place : Zip
    <svg width="14" height="14" viewBox="0 0 14 14"><circle cx="6" cy="6" r="4.3" fill="none" stroke="#fff" stroke-width="1.8"/><line x1="9.2" y1="9.2" x2="13" y2="13" stroke="#fff" stroke-width="2"/></svg>
  </div>
</div>

<header class="abs header">
  <div class="abs brand"><div class="mark"></div><div class="name">BRIGHTWELL GIVING</div></div>
  <div class="abs tagline">Giving Close to Home, Caring Far Away</div>
  <nav>
    <div class="abs nav" style="left:506px">MISSION</div>
    <div class="abs nav" style="left:577px">HOW IT WORKS</div>
    <div class="abs nav" style="left:681px">ABOUT US</div>
    <div class="abs nav" style="left:761px">SPONSORS</div>
    <div class="abs nav" style="left:845px">NEWS</div>
    <div class="abs nav" style="left:904px">WALL OF NEEDS</div>
  </nav>
  <div class="abs donate">DONATE</div>
</header>

<div class="abs crumb"><span>HOME</span> / MISSION</div>

<div class="abs photo" role="img" aria-label="Hands of different people stacked together over a world map" style="left:127px;top:217px;width:597px;height:337px;background:linear-gradient(135deg,#2f62a8 0%,#4b8c4a 40%,#b98a5a 60%,#2f5ea6 100%)"></div>
<section class="abs mission-card">
  <h1 class="h-gold">Mission Statement</h1>
  <p class="body">Brightwell Giving has a two part mission to help local communities while helping the planet. The average American discards 68 lbs of clothing annually. That is 1,325,340,196 lbs for New York State alone and 21,202,400,000 lbs for the U.S. every year! By keeping unwanted clothes out of the trash can we are greatly reducing the amount of material that enters our landfills. We are also turning the unwanted clothes into funding for our local communities. We are asking for your help to increase local support. Simply put, there is no better time to act than now.</p>
</section>

<section class="abs impact">
  <h2 class="h-gold">Impact Statement</h2>
  <p class="body">In such trying times as these, the only people we can turn to for help are each other. Nothing is greater than the desire of a community to help its own. Brightwell Giving is dedicated to becoming an active member of the community by providing for its less fortunate members. Our goal is to differentiate ourselves from other charitable organizations by running a transparent operation that makes the most of its donations. Our plan is to run an “open book” charity wherein all of our operations and accounting system are fully disclosed to the public. This will allow the community and its donors to see where your donations are going. Anyone will be able to review the operating costs of our organization in order to ensure that we are giving the most amount possible to the community’s beneficiaries. A non-profit organization is only effective when it benefits the people that need it most. With your help, we can accomplish that goal. Brightwell Giving aims to bring back the spirit of giving to our community, one family at a time.</p>
</section>

<div class="abs divider"></div>

<div class="abs photo" role="img" aria-label="Video still of a church building front in Haiti" style="left:126px;top:830px;width:476px;height:267px;background:linear-gradient(160deg,#3a3f4a 0%,#8a6a5a 45%,#c9a48a 70%,#4a5a3a 100%)"></div>
<div class="abs video-title">First visit to Haiti 01 21 2017</div>
<svg class="abs" style="left:336px;top:940px" width="56" height="40" viewBox="0 0 56 40"><rect width="56" height="40" rx="8" fill="#212121" opacity=".8"/><path d="M22 12 L36 20 L22 28Z" fill="#fff"/></svg>
<section class="abs story" style="left:624px;top:868px">
  <h2>Haiti statements</h2>
  <p class="body">Here is the statement to introduce the Haiti project.<br>Greenfield Learning Centre (G.L.C) is a non Governmental Organisation. Where young adult students can learn how to produce foods including vegetables and grow plants to protect the environment. Associate with Brightwell Giving, we will introduce a new modern farming in Haiti. We will open to an international exchange.</p>
  <span class="more">Read more</span>
</section>

<section class="abs story" style="left:127px;top:1244px">
  <h2>Ukraine statements</h2>
  <p class="body">Brought humanitarian aid to large families. Glory to the Lord for the opportunity. Social assistance is the door to the preaching of the gospel. When you come to the needy not with empty hands, their hearts are located to hear the Word of God. So you do what the Lord commanded: to do good to the poor.</p>
  <span class="more">Read more</span>
</section>
<div class="abs photo" role="img" aria-label="Three volunteers seated behind bags of donated clothes" style="left:602px;top:1150px;width:472px;height:353px;background:linear-gradient(180deg,#c7c9cc 0%,#9a9da2 45%,#2a2a2e 75%,#1e1e22 100%)"></div>

<div class="abs photo" role="img" aria-label="Mother holding her young daughter on a sofa" style="left:127px;top:1558px;width:472px;height:288px;background:linear-gradient(170deg,#7a5a3a 0%,#a88a68 40%,#e6dcc2 70%,#c9bea0 100%)"></div>
<section class="abs story" style="left:624px;top:1594px">
  <h2>LOVE THY NEIGHBOR-SOFIA</h2>
  <p class="body">Hello Brightwell Giving team. I am a mother of two girls, one of whom has a difficult genetic disorder. Just a few years ago at the age of 4 my daughter couldn't hold her head up on her own. While doing therapy in the rehabilitation facility, her health significantly improved. Today she holds up her head on her own, she's able to crawl and get on her feet when holding on to support. However in order for my daughter to walk she will require very expensive rehabilitation.</p>
  <span class="more">Read more</span>
</section>

<div class="abs mapbar">
  <svg class="abs" style="left:14px;top:12px" width="18" height="14" viewBox="0 0 18 14"><rect x="1" y="1" width="16" height="12" fill="none" stroke="#fff" stroke-width="1.6"/><line x1="6" y1="1" x2="6" y2="13" stroke="#fff" stroke-width="1.6"/></svg>
  <div class="abs" style="left:53px;top:10px">Brightwell Giving…</div>
  <svg class="abs" style="left:1134px;top:11px" width="16" height="16" viewBox="0 0 16 16"><circle cx="12" cy="3" r="2.2" fill="#fff"/><circle cx="4" cy="8" r="2.2" fill="#fff"/><circle cx="12" cy="13" r="2.2" fill="#fff"/><path d="M12 3 L4 8 L12 13" stroke="#fff" stroke-width="1.4" fill="none"/></svg>
  <svg class="abs" style="left:1163px;top:11px" width="16" height="16" viewBox="0 0 16 16" fill="none" stroke="#fff" stroke-width="1.8"><path d="M1 5V1h4M11 1h4v4M15 11v4h-4M5 15H1v-4"/></svg>
</div>
<div class="abs map" role="img" aria-label="Road map of the northeastern region marking local donation bin locations" style="background:linear-gradient(90deg,#e4e1d8 0%,#dfe3d6 50%,#e6e3da 100%)"></div>

<footer class="abs footer">
  <div class="abs" style="left:127px;top:22px">© 2018 BRIGHTWELL GIVING. ALL RIGHTS RESERVED.</div>
  <div class="abs" style="left:1050px;top:16px;width:21px;height:21px;background:var(--white);border-radius:3px"></div>
</footer>

</body>
</html>
```